Save the Date card

This will be a Save the Date 5x7 card...preferably Hunter Green background

Annual Fund Leadership Dinner
June 20, 2023. 6:30 pm
Location: The Pellimore's Home
4187 Brindlecove Ridge Rd
Harrison, TN 37598

Other side of card:
We would prayerfully ask that you consider partnering with us as we kick off our Annual Fund this Fall to celebrate our 25 year anniversary as an Academy.
Please direct any questions to Marla Quenby, our Director of Advancement 423-555-0184 x 3617 or advancement@corvellanprep.org

```html
<!DOCTYPE html>
<html lang="en">
<head>
<meta charset="utf-8">
<title>Save the Date – Annual Fund Leadership Dinner</title>
<link rel="stylesheet" href="https://fonts.googleapis.com/css2?family=Montserrat:wght@400;500;600;700;800&display=swap">
<style>
  :root {
    --backdrop: #a3a3a3;
    --hunter: #193a23;
    --hunter-text: #1a3a24;
    --gold: #ad9c5c;
    --paper: #f3f2f2;
    --white: #ffffff;
  }
  * { margin: 0; padding: 0; box-sizing: border-box; }
  html, body { width: 1200px; height: 902px; overflow: hidden; }
  body {
    background: var(--backdrop);
    font-family: "Montserrat", sans-serif;
    position: relative;
  }
  .card {
    position: absolute;
    left: 78px; top: 57px;
    width: 1043px; height: 744px;
    background: var(--paper);
    box-shadow: 6px 8px 10px rgba(0,0,0,0.35);
    overflow: hidden;
  }
  .card__band {
    position: absolute;
    left: 0; top: 0; width: 100%; height: 459px;
    background: linear-gradient(180deg, #183822 0%, #1b3d25 60%, #1f4229 100%);
  }
  .card__frame {
    position: absolute;
    left: 44px; top: 58px; width: 955px; height: 642px;
    border: 1.5px solid var(--gold);
  }
  .eyebrow {
    position: absolute;
    left: 0; top: 37px; width: 100%;
    text-align: center;
  }
  .eyebrow span {
    display: inline-block;
    background: var(--hunter);
    padding: 0 18px;
    color: var(--gold);
    font-weight: 600;
    font-size: 39px;
    letter-spacing: 2.5px;
    line-height: 44px;
  }
  .title {
    position: absolute;
    left: 80px; top: 0;
    width: 480px; height: 400px;
  }
  .title__line {
    position: absolute;
    left: 0;
    line-height: 1;
    white-space: nowrap;
  }
  .title__line--lead {
    top: 154px;
    color: var(--white);
    font-weight: 500;
    font-size: 60px;
    letter-spacing: -0.5px;
    text-shadow: 2px 3px 6px rgba(0,0,0,0.35);
  }
  .title__line--main {
    color: var(--gold);
    font-weight: 800;
    font-size: 70px;
    letter-spacing: -2px;
    text-shadow: 3px 4px 6px rgba(0,0,0,0.4);
  }
  .title__line--leadership { top: 217px; }
  .title__line--dinner { top: 292px; }
  .date-tag {
    position: absolute;
    left: 85px; top: 428px;
    width: 357px; height: 62px;
    background: var(--gold);
    box-shadow: 3px 7px 8px rgba(0,0,0,0.35);
    color: var(--white);
    font-weight: 700;
    font-size: 40px;
    line-height: 62px;
    text-align: center;
    letter-spacing: 0.5px;
  }
  .time {
    position: absolute;
    left: 86px; top: 510px;
    color: var(--hunter-text);
    font-weight: 600;
    font-size: 35px;
    letter-spacing: 0.8px;
    display: flex; align-items: center;
  }
  .time__divider {
    display: inline-block;
    width: 2px; height: 32px;
    background: var(--gold);
    margin: 0 16px;
  }
  .venue {
    position: absolute;
    left: 87px; top: 595px;
    display: flex; gap: 9px;
  }
  .venue__pin { width: 22px; height: 27px; margin-top: 4px; }
  .venue__address {
    font-style: normal;
    color: var(--hunter-text);
    font-size: 23px;
    line-height: 30px;
    letter-spacing: 0.8px;
  }
  .web {
    position: absolute;
    left: 627px; top: 653px;
    color: var(--hunter-text);
    font-size: 25.5px;
    letter-spacing: 0.8px;
    font-weight: 500;
  }
  .web strong { color: var(--gold); font-weight: 600; }
  .crest {
    position: absolute;
    left: 592px; top: 122px;
    width: 374px; height: 492px;
    overflow: visible;
  }
</style>
</head>
<body>
  <section class="card">
    <div class="card__band"></div>
    <div class="card__frame"></div>

    <p class="eyebrow"><span>SAVE THE DATE</span></p>

    <h1 class="title">
      <span class="title__line title__line--lead">ANNUAL FUND</span>
      <span class="title__line title__line--main title__line--leadership">LEADERSHIP</span>
      <span class="title__line title__line--main title__line--dinner">DINNER</span>
    </h1>

    <p class="date-tag">JUNE 20, 2023</p>

    <p class="time">TUESDAY<span class="time__divider"></span>6:30 p.m.</p>

    <div class="venue">
      <svg class="venue__pin" viewBox="0 0 22 27" aria-hidden="true">
        <path d="M11 1C5.5 1 1.5 5 1.5 10.2 1.5 17 11 26 11 26s9.5-9 9.5-15.8C20.5 5 16.5 1 11 1z" fill="#ad9c5c"/>
        <circle cx="11" cy="10" r="3.8" fill="#f3f2f2"/>
      </svg>
      <address class="venue__address">
        The Pellimore’s Home<br>
        4187 Brindlecove Ridge Rd<br>
        Harrison, TN 37598
      </address>
    </div>

    <p class="web">www.<strong>corvellanprep</strong>.org</p>

    <svg class="crest" viewBox="0 0 374 492" role="img" aria-label="Photo of an elegant dinner table set with crystal glasses, white plates and a floral centerpiece">
      <defs>
        <linearGradient id="tablePhoto" x1="0" y1="0" x2="0" y2="1">
          <stop offset="0" stop-color="#141312"/>
          <stop offset="0.45" stop-color="#1c1a16"/>
          <stop offset="0.7" stop-color="#4a3324"/>
          <stop offset="1" stop-color="#1a1410"/>
        </linearGradient>
      </defs>
      <path d="M28,70 Q187,12 346,70 L346,270 C346,370 250,425 187,462 C124,425 28,370 28,270 Z"
            fill="none" stroke="#ad9c5c" stroke-width="56" stroke-linejoin="round"/>
      <path d="M28,70 Q187,12 346,70 L346,270 C346,370 250,425 187,462 C124,425 28,370 28,270 Z"
            fill="none" stroke="#ffffff" stroke-width="28" stroke-linejoin="round"/>
      <path d="M28,70 Q187,12 346,70 L346,270 C346,370 250,425 187,462 C124,425 28,370 28,270 Z"
            fill="url(#tablePhoto)"/>
    </svg>
  </section>
</body>
</html>
```